Webdesign - brightparcelhub.com.au - Minimalist

I need someone to make a website for me - I opened an account on brightparcelhub.com.au, paid hundreds and I don't know how to make a webstore.
Someone please help me.

The design is easy.

Minimalist - White background - Black writing.

Font - Brush strokes. Not too fat.

Pages: Home - Shop - Check Out - Contact Us

Let me know if you need more info.
Updates

Target Market(s)

Females aged between 18 ~ 38

Industry/Entity Type

Shop

Font styles to use
Other font styles liked:
• Custom Brush Stroke

Requirements
Must have
• Must be minimalist white background with black writing.

Font must be something of Brush Strokes, I will leave the specific design up to the artists.

```html
<!DOCTYPE html>
<html lang="en">
<head>
<meta charset="utf-8">
<title>Kalora Online – Necklaces Designs</title>
<link rel="stylesheet" href="https://fonts.googleapis.com/css2?family=Lato:wght@400;700&family=Arimo:wght@400;700&display=swap">
<style>
:root{
  --ink:#111111;
  --muted:#555555;
  --line:#cfcfcf;
  --card-border:#d6d6d6;
  --band:#efefef;
  --footer:#e8e8e8;
  --white:#ffffff;
  --icon:#b9c4d0;
}
*{box-sizing:border-box;margin:0;padding:0}
html,body{width:1200px;height:794px;overflow:hidden;background:var(--white)}
body{position:relative;font-family:'Lato',sans-serif;color:var(--ink)}
.abs{position:absolute}

.brand{left:210px;top:8px;display:flex;align-items:center;gap:12px}
.brand-dot{width:46px;height:46px;border-radius:50%;border:4px solid var(--ink)}
.brand-name{font-weight:700;font-size:27px;color:var(--ink);letter-spacing:.3px}

.main-nav{left:210px;top:70px;display:flex;font-size:12px}
.main-nav a{color:var(--ink);text-decoration:none;margin-right:44px}
.main-nav a.active{font-weight:700;text-decoration:underline;text-underline-offset:3px}

.bag{left:782px;top:20px;display:flex;align-items:center;gap:6px}
.bag-text{text-align:right;font-size:9.5px;line-height:11px;color:#333}
.social{left:880px;top:21px;display:flex;gap:2px}
.social span{width:23px;height:25px;background:var(--icon);border-radius:3px}

.search{left:848px;top:65px;width:142px;height:16px;border-radius:8px;background:var(--ink);color:#bbb;font-size:7px;padding:4px 0 0 10px;white-space:nowrap}
.search svg{position:absolute;right:6px;top:3px}

.pattern-band{left:0;top:102px;width:1200px;height:632px;background:linear-gradient(180deg,var(--band) 0%,#f7f7f7 40%,#ffffff 100%)}

.crumbs{left:217px;top:112px;font-size:9.5px;color:#888;white-space:nowrap}
.crumbs b{color:#333;font-weight:700}
.rule{left:210px;width:780px;height:1px;background:var(--line)}
.page-title{left:215px;top:134px;font-size:19px;font-weight:400;color:#444;letter-spacing:-.2px;white-space:nowrap}
.results{left:217px;top:173px;font-size:9px;letter-spacing:-.3px;color:#444;white-space:nowrap}
.sort{left:326px;top:171px;width:138px;height:15px;border:1px solid #bbb;background:var(--white);font-size:8px;color:#555;padding:2px 4px;white-space:nowrap}
.sort i{position:absolute;right:2px;top:2px;width:10px;height:9px;border:1px solid #999;font-style:normal;font-size:6px;line-height:8px;text-align:center}

.product{width:251px}
.product-photo{height:120px;border:1px solid var(--card-border);border-radius:5px;background:radial-gradient(circle at 50% 50%,#e6e1d6 0%,#f6f6f6 45%,#ffffff 75%)}
.product-photo.silver{background:radial-gradient(circle at 50% 50%,#d8dadd 0%,#f4f4f5 45%,#ffffff 75%)}
.product-name{margin-top:10px;text-align:center;font-weight:700;font-size:11.5px;white-space:nowrap}
.product-price{text-align:center;font-size:9.5px;margin-top:3px}
.product-price b{font-size:11px;margin-left:3px}
.product-actions{display:flex;justify-content:center;gap:6px;margin-top:8px}
.btn{width:72px;height:17px;border-radius:4px;background:var(--ink);color:var(--white);font-size:9px;text-align:center;line-height:17px;white-space:nowrap}

.site-footer{left:0;top:734px;width:1200px;height:60px;background:var(--footer);font-family:'Arimo',sans-serif;font-size:10px;color:#222}
.site-footer p{position:absolute;left:209px;top:25px;white-space:nowrap}
</style>
</head>
<body>

<header>
  <div class="abs brand"><span class="brand-dot"></span><span class="brand-name">Kalora Online</span></div>

  <nav class="abs main-nav">
    <a href="#">Home</a><a href="#" class="active">SHOP</a><a href="#">CHECK OUT</a><a href="#">CONTACT US</a>
  </nav>

  <div class="abs bag">
    <svg width="22" height="20" viewBox="0 0 22 20"><path d="M1 2h4l3 11h10l2-8H7" fill="none" stroke="#222" stroke-width="2"/><rect x="8" y="5" width="10" height="7" fill="#222"/><circle cx="9" cy="17" r="2" fill="#222"/><circle cx="17" cy="17" r="2" fill="#222"/></svg>
    <div class="bag-text">your bag<br>0 items ($0.00)</div>
  </div>

  <div class="abs social"><span></span><span></span><span></span><span></span></div>

  <div class="abs search">Search entire store here
    <svg width="10" height="10" viewBox="0 0 10 10"><circle cx="6" cy="4" r="3" fill="none" stroke="#fff" stroke-width="1.3"/><path d="M4 6L1 9" stroke="#fff" stroke-width="1.5"/></svg>
  </div>
</header>

<div class="abs pattern-band" role="img" aria-label="Faint pale grey damask background texture"></div>

<main>
  <div class="abs crumbs">home / shop / <b>shoes</b></div>
  <div class="abs rule" style="top:130px"></div>
  <h1 class="abs page-title">Necklaces Designs</h1>
  <div class="abs rule" style="top:166px"></div>
  <div class="abs results">Showing 1–10 of 20 results</div>
  <div class="abs sort">Default sorting<i>▼</i></div>

  <article class="abs product" style="left:210px;top:225px">
    <div class="product-photo" role="img" aria-label="Gold necklace with interlocking rings pendant"></div>
    <h2 class="product-name">MOONLACE BRACELET SH-001</h2>
    <p class="product-price">retail price&nbsp; : <b>$75.00</b></p>
    <div class="product-actions"><span class="btn">add to cart</span><span class="btn">view details</span></div>
  </article>
  <article class="abs product" style="left:475px;top:225px">
    <div class="product-photo silver" role="img" aria-label="Silver swirl pendant with clear stone"></div>
    <h2 class="product-name">MOONLACE BRACELET SH-001</h2>
    <p class="product-price">retail price&nbsp; : <b>$75.00</b></p>
    <div class="product-actions"><span class="btn">add to cart</span><span class="btn">view details</span></div>
  </article>
  <article class="abs product" style="left:740px;top:225px">
    <div class="product-photo silver" role="img" aria-label="Silver chain with solitaire crystal pendant"></div>
    <h2 class="product-name">MOONLACE BRACELET SH-001</h2>
    <p class="product-price">retail price&nbsp; : <b>$75.00</b></p>
    <div class="product-actions"><span class="btn">add to cart</span><span class="btn">view details</span></div>
  </article>

  <article class="abs product" style="left:210px;top:450px">
    <div class="product-photo silver" role="img" aria-label="Silver leaf pendant with blue stone"></div>
    <h2 class="product-name">MOONLACE BRACELET SH-001</h2>
    <p class="product-price">retail price&nbsp; : <b>$75.00</b></p>
    <div class="product-actions"><span class="btn">add to cart</span><span class="btn">view details</span></div>
  </article>
  <article class="abs product" style="left:475px;top:450px">
    <div class="product-photo" role="img" aria-label="Gold twisted pendant set with small crystals"></div>
    <h2 class="product-name">MOONLACE BRACELET SH-001</h2>
    <p class="product-price">retail price&nbsp; : <b>$75.00</b></p>
    <div class="product-actions"><span class="btn">add to cart</span><span class="btn">view details</span></div>
  </article>
  <article class="abs product" style="left:740px;top:450px">
    <div class="product-photo silver" role="img" aria-label="Silver bow pendant covered in crystals"></div>
    <h2 class="product-name">MOONLACE BRACELET SH-001</h2>
    <p class="product-price">retail price&nbsp; : <b>$75.00</b></p>
    <div class="product-actions"><span class="btn">add to cart</span><span class="btn">view details</span></div>
  </article>
</main>

<footer class="abs site-footer">
  <p>© 2014, Kalora Online, P.O . <b>Box 0000, XXXXXX, XX 00000</b></p>
</footer>

</body>
</html>
```